2 Business Card Designs

Need two business cards designed:
1) for lumora films (wedding video) website is lumorafilms.com.au
2) for lumora films (corporate video) website is lumorafilms.net.au

I am looking for something simple, no fancy shapes etc. Just elegant, simple and classy.

Both companies are video companies, one specialising in weddings the other corporate videos. Neither card needs to have any pics of video or camera related images. Please use same colour schemes as respective websites.

Logo is the same but can change colour.

Industry/Entity Type

Camera

Requirements
Must have
• Logo should be either all white or a colour to match websites
Should not have
• swirls, flowers, shapes, etc.

```html
<!DOCTYPE html>
<html lang="en">
<head>
<meta charset="utf-8">
<title>Lumora Films – Business Card</title>
<link rel="stylesheet" href="https://fonts.googleapis.com/css2?family=Questrial&family=Pathway+Gothic+One&display=swap">
<style>
  :root {
    --page: #ffffff;
    --card: #e1e3c9;
    --card-edge: #b9bbab;
    --ink: #4a4a46;
    --band: #bfc1a9;
    --band-light: #d3d5bd;
    --bar-dark: #6e6e62;
    --bar-light: #c9cbb3;
    --url: #f2f3e6;
    --reel-dark: #8b907f;
    --reel-light: #c6c9b8;
  }
  * { margin: 0; padding: 0; box-sizing: border-box; }
  html, body {
    width: 945px;
    height: 1200px;
    overflow: hidden;
    background: var(--page);
  }
  .sheet {
    position: relative;
    width: 945px;
    height: 1200px;
  }
  .card {
    position: absolute;
    left: 46px;
    width: 851px;
    height: 542px;
    background: var(--card);
    border: 2px solid var(--card-edge);
    border-radius: 36px;
    box-shadow: 0 2px 6px rgba(0, 0, 0, 0.18);
    overflow: hidden;
  }
  .card--front { top: 37px; }
  .card--back { top: 619px; }

  /* Front */
  .header-band {
    position: absolute;
    left: 16px;
    top: 62px;
    width: 823px;
    height: 48px;
    background: linear-gradient(90deg, var(--band), var(--band-light) 50%, var(--band));
  }
  .wordmark {
    position: absolute;
    left: 0;
    right: 0;
    top: 118px;
    text-align: center;
    font-family: "Questrial", sans-serif;
    font-weight: 400;
    color: var(--ink);
  }
  .wordmark__name {
    display: block;
    font-size: 215px;
    line-height: 180px;
    letter-spacing: 6px;
  }
  .wordmark__line {
    display: block;
    margin-top: 8px;
    font-size: 72px;
    line-height: 72px;
    letter-spacing: 84px;
    padding-left: 84px;
  }
  .web-bar {
    position: absolute;
    left: 17px;
    top: 407px;
    width: 640px;
    height: 48px;
    background: linear-gradient(90deg, var(--bar-dark) 0%, #8d8d80 35%, var(--bar-light) 100%);
  }
  .web-bar__url {
    position: absolute;
    left: 185px;
    top: 0;
    line-height: 48px;
    font-family: "Questrial", sans-serif;
    font-size: 30px;
    letter-spacing: 1.5px;
    color: var(--url);
    white-space: nowrap;
  }

  /* Back */
  .contact {
    position: absolute;
    left: 86px;
    top: 124px;
    list-style: none;
    font-family: "Pathway Gothic One", sans-serif;
    font-size: 44px;
    line-height: 57px;
    color: var(--ink);
  }
  .reel {
    position: absolute;
    left: 466px;
    top: 96px;
    width: 280px;
    height: 342px;
  }
</style>
</head>
<body>
<main class="sheet">
  <section class="card card--front" aria-label="Card front">
    <div class="header-band" role="img" aria-label="Chevron pattern band"></div>
    <h1 class="wordmark">
      <span class="wordmark__name">lumora</span>
      <span class="wordmark__line">FILMS</span>
    </h1>
    <div class="web-bar">
      <span class="web-bar__url">www.LumoraFilms.com.au</span>
    </div>
  </section>

  <section class="card card--back" aria-label="Card back">
    <ul class="contact">
      <li>Comapany name</li>
      <li>Address</li>
      <li>Sample name</li>
      <li>Phone#</li>
      <li>Website</li>
    </ul>
    <svg class="reel" viewBox="0 0 280 342" role="img" aria-label="Curled film strip illustration">
      <defs>
        <linearGradient id="reel-tone" x1="0" y1="0" x2="1" y2="1">
          <stop offset="0" stop-color="var(--reel-light)"/>
          <stop offset="1" stop-color="var(--reel-dark)"/>
        </linearGradient>
      </defs>
      <rect x="20" y="12" width="240" height="318" rx="10" fill="url(#reel-tone)" transform="rotate(4 140 171)"/>
    </svg>
  </section>
</main>
</body>
</html>
```